Business Card Design
Brightvale Marks
Modern
Kemi Varo
47 Olumide Bankole Crescent
Wuse 2
Abuja
Nigeria
info@brightvalemarks.com
www.brightvalemarks.com

```html
<!DOCTYPE html>
<html lang="en">
<head>
<meta charset="utf-8">
<title>Brightvale Marks – Business Card</title>
<link rel="stylesheet" href="https://fonts.googleapis.com/css2?family=Tinos:wght@400;700&display=swap">
<style>
  :root {
    --bg: #e9e6e1;
    --blue-light: #2a9ad8;
    --blue-dark: #0b6aae;
    --green: #8dc63f;
    --white: #ffffff;
    --ink-light: #eaf5fc;
    --brand: #1a7fc4;
  }
  * { margin: 0; padding: 0; box-sizing: border-box; }
  html, body { width: 1200px; height: 871px; overflow: hidden; }
  body {
    background: var(--bg);
    font-family: "Tinos", "Times New Roman", serif;
    position: relative;
  }
  .card {
    position: absolute;
    width: 640px;
    height: 366px;
    box-shadow: 0 6px 18px rgba(0,0,0,0.18);
    overflow: hidden;
  }
  .card-back {
    left: 280px;
    top: 40px;
    background: radial-gradient(ellipse at 35% 40%, var(--blue-light), var(--blue-dark));
    display: flex;
    align-items: center;
    justify-content: center;
  }
  .card-front {
    left: 280px;
    top: 446px;
    background: var(--white);
    display: flex;
  }
  .front-info {
    width: 62%;
    height: 100%;
    background: radial-gradient(ellipse at 40% 35%, var(--blue-light), var(--blue-dark));
    color: var(--ink-light);
    padding: 34px 0 0 40px;
    position: relative;
  }
  .front-divider {
    width: 6px;
    height: 100%;
    background: var(--white);
    border-right: 4px solid var(--green);
  }
  .front-brand {
    flex: 1;
    display: flex;
    align-items: center;
    justify-content: center;
    gap: 10px;
  }
  .person-name {
    font-weight: 700;
    font-size: 22px;
    color: var(--white);
  }
  .address {
    margin-top: 46px;
    font-size: 15px;
    line-height: 1.35;
  }
  .contacts {
    position: absolute;
    left: 40px;
    bottom: 30px;
    list-style: none;
    font-size: 14px;
    line-height: 1.4;
  }
  .contacts li { display: flex; align-items: center; gap: 7px; }
  .contacts svg { width: 11px; height: 11px; }
  .brand-mark {
    width: 14px;
    height: 14px;
    border-radius: 50%;
    background: var(--green);
    flex: none;
  }
  .brand-name {
    font-size: 24px;
    font-weight: 400;
    color: var(--brand);
    text-transform: uppercase;
    letter-spacing: 0.5px;
  }
  .back-brand {
    display: flex;
    align-items: center;
    gap: 12px;
  }
  .back-brand .brand-name { color: var(--white); font-size: 28px; }
  .back-brand .brand-mark { background: var(--white); width: 18px; height: 18px; }
</style>
</head>
<body>
  <section class="card card-back" aria-label="Card back">
    <div class="back-brand">
      <span class="brand-mark"></span>
      <span class="brand-name">Brightvale Marks</span>
    </div>
  </section>

  <section class="card card-front" aria-label="Card front">
    <div class="front-info">
      <p class="person-name">Kemi Varo</p>
      <p class="address">47 Olumide Bankole Crescent<br>Wuse 2 Abuja Nigeria</p>
      <ul class="contacts">
        <li>
          <svg viewBox="0 0 12 12" aria-hidden="true"><path d="M3 1l2 2.5-1 1.2a7 7 0 0 0 3.3 3.3l1.2-1L11 9l-1.2 1.8C5.5 11 1 6.5 1.2 2.2z" fill="#eaf5fc"/></svg>
          08150004217
        </li>
        <li>
          <svg viewBox="0 0 12 12" aria-hidden="true"><rect x="1" y="2.5" width="10" height="7" fill="none" stroke="#eaf5fc" stroke-width="1.2"/><path d="M1 2.5l5 4 5-4" fill="none" stroke="#eaf5fc" stroke-width="1.2"/></svg>
          info@brightvalemarks.com
        </li>
        <li>
          <svg viewBox="0 0 12 12" aria-hidden="true"><circle cx="6" cy="6" r="4.6" fill="none" stroke="#eaf5fc" stroke-width="1.2"/><path d="M1.4 6h9.2M6 1.4c-2.4 2.6-2.4 6.6 0 9.2M6 1.4c2.4 2.6 2.4 6.6 0 9.2" fill="none" stroke="#eaf5fc" stroke-width="0.9"/></svg>
          www.brightvalemarks.com
        </li>
      </ul>
    </div>
    <div class="front-divider"></div>
    <div class="front-brand">
      <span class="brand-mark"></span>
      <span class="brand-name">Brightvale Marks</span>
    </div>
  </section>
</body>
</html>
```